Business Card Design

I need a business card design for a new company based in Australind, Western Australia. The business is for puppet shows at children's parties, fetes, custom puppet builds, etc.Attached is a picture of Ray Pellow in silhouette. I was thinking a design of a puppeteer at the top of some stairs talking to a puppet in silhouette but open to suggestions. (Lantern Loft is named as I do all my puppet builds in the top room of my house (at the Lantern Loft).

Industry/Entity Type

Business

Contact Information for Business Card

Lantern Loft Marionettes, Dale Voss, Puppeteer / Puppet Builder, phone - 0438562703, Puppet shows / Custom Puppet Builds, Working With Children

Requirements
Must have
• Name and Logo on one side. Second side to have business card details.

```html
<!DOCTYPE html>
<html lang="en">
<head>
<meta charset="utf-8">
<title>Lantern Loft Marionettes – Business Cards</title>
<link href="https://fonts.googleapis.com/css2?family=Questrial&display=swap" rel="stylesheet">
<style>
  :root {
    --page-bg: #ecebe8;
    --brand-red: #9c1f24;
    --brand-red-dark: #86181c;
    --card-white: #ffffff;
    --ink: #1d1d1d;
    --ink-soft: #3a3a3a;
    --on-red: #ffffff;
  }
  * { margin: 0; padding: 0; box-sizing: border-box; }
  html, body {
    width: 1200px;
    height: 900px;
    overflow: hidden;
    background: var(--page-bg);
    font-family: "Questrial", "Century Gothic", sans-serif;
  }
  .canvas {
    position: relative;
    width: 1200px;
    height: 900px;
  }
  .card {
    position: absolute;
    width: 640px;
    height: 366px;
    border-radius: 22px;
    box-shadow: 0 6px 18px rgba(0,0,0,0.18);
    display: flex;
    flex-direction: column;
    align-items: center;
  }
  .card--front {
    left: 170px;
    top: 60px;
    background: linear-gradient(135deg, var(--brand-red) 0%, var(--brand-red-dark) 100%);
    color: var(--on-red);
    padding-top: 88px;
  }
  .card--back {
    left: 390px;
    top: 474px;
    background: var(--card-white);
    color: var(--ink);
    padding-top: 70px;
  }
  .brand {
    display: flex;
    align-items: center;
    gap: 16px;
  }
  .brand__mark {
    width: 44px;
    height: 44px;
  }
  .card--front .brand__mark { background: var(--on-red); }
  .card--back .brand__mark { background: var(--brand-red); }
  .brand__name {
    font-size: 34px;
    line-height: 1;
    letter-spacing: 0.5px;
  }
  .card--front .brand__name { color: var(--on-red); }
  .card--back .brand__name { color: var(--ink); }
  .services {
    margin-top: 70px;
    font-size: 17px;
    letter-spacing: 0.6px;
    text-align: center;
  }
  .wwc-number {
    margin-top: 8px;
    font-size: 19px;
    letter-spacing: 1px;
  }
  .contact {
    margin-top: 62px;
    align-self: flex-start;
    margin-left: 170px;
  }
  .contact__name {
    font-size: 38px;
    color: var(--ink);
    letter-spacing: 0.5px;
  }
  .contact__role {
    margin-top: 4px;
    font-size: 21px;
    color: var(--brand-red);
    letter-spacing: 0.6px;
  }
  .contact__phone {
    margin-top: 8px;
    display: flex;
    align-items: center;
    gap: 10px;
    font-size: 27px;
    color: var(--ink-soft);
    letter-spacing: 1.5px;
  }
  .contact__phone svg { width: 32px; height: 26px; }
</style>
</head>
<body>
<main class="canvas">
  <section class="card card--front" aria-label="Card front">
    <div class="brand">
      <span class="brand__mark"></span>
      <span class="brand__name">Lantern Loft Marionettes</span>
    </div>
    <p class="services">Puppet shows / Custom Puppet Builds, Working With Children</p>
    <p class="wwc-number">3917265</p>
  </section>

  <section class="card card--back" aria-label="Card back">
    <div class="brand">
      <span class="brand__mark"></span>
      <span class="brand__name">Lantern Loft Marionettes</span>
    </div>
    <div class="contact">
      <p class="contact__name">Dale Voss,</p>
      <p class="contact__role">Puppeteer / Puppet Builder</p>
      <p class="contact__phone">
        <svg viewBox="0 0 32 26" aria-hidden="true">
          <path d="M2 9 C2 3 30 3 30 9 L30 11 L23 11 L23 8 L9 8 L9 11 L2 11 Z" fill="var(--brand-red)"/>
          <path d="M8 11 L24 11 L29 24 L3 24 Z" fill="var(--brand-red)"/>
          <circle cx="16" cy="17" r="3.5" fill="var(--card-white)"/>
        </svg>
        0438562703
      </p>
    </div>
  </section>
</main>
</body>
</html>
```